Postcard bar mitzvah invitations

I'm looking for glossy postcards which which contain information for my son's bar mitzvah - the time and place of the service, that it will be followed by a luncheon, the time and place of the party, and how to RSVP.

```html
<!DOCTYPE html>
<html lang="en">
<head>
<meta charset="utf-8">
<title>Bar Mitzvah Invitation</title>
<link href="https://fonts.googleapis.com/css2?family=Marcellus&family=Marcellus+SC&family=Arimo:ital,wght@0,400;1,700&display=swap" rel="stylesheet">
<style>
  :root {
    --page-bg: #efede8;
    --card-deep: #04084f;
    --card-mid: #0a1a9e;
    --text-silver: #c6c9d4;
    --name-blue: #35b6ea;
    --accent-blue: #1e94cf;
  }
  * { margin: 0; padding: 0; box-sizing: border-box; }
  html, body {
    width: 1200px; height: 1015px; overflow: hidden;
    background: var(--page-bg);
  }
  .invitation {
    position: absolute; left: 94px; top: 100px;
    width: 1033px; height: 798px;
    background: radial-gradient(ellipse 55% 65% at 70% 55%, var(--card-mid) 0%, #071287 45%, var(--card-deep) 100%);
    overflow: hidden;
  }
  .star-pattern { position: absolute; left: 0; top: 0; }
  .details {
    position: absolute; left: 411px; top: 0; width: 600px;
    text-align: center; color: var(--text-silver);
  }
  .line { position: absolute; left: 0; width: 100%; white-space: nowrap; line-height: 1.2; }
  .caps { font-family: "Marcellus SC", serif; letter-spacing: 1px; }
  .caps.small { font-size: 18px; }
  .caps.medium { font-size: 20px; letter-spacing: 1.2px; }
  .honoree { font-family: "Marcellus", serif; font-size: 46px; font-weight: 400; color: var(--name-blue); }
  .hosts { font-family: "Marcellus", serif; font-size: 35px; }
  .hosts .amp { font-style: italic; font-size: 40px; }
  .rsvp-deadline { font-family: "Arimo", sans-serif; font-weight: 700; font-style: italic; font-size: 20px; letter-spacing: 1px; }
  .contact { font-family: "Arimo", sans-serif; font-size: 21px; letter-spacing: 0.5px; }
  .contact.phone { letter-spacing: 2.5px; }
  .phone-icon { display: inline-block; vertical-align: -6px; margin-right: 2px; }
  .emblem { position: absolute; left: 270px; top: 556px; width: 66px; height: 70px; }
</style>
</head>
<body>
  <main class="invitation">
    <svg class="star-pattern" width="525" height="798" viewBox="0 0 525 798" role="img" aria-label="Decorative pattern of interlocking white and blue six-pointed stars">
      <defs>
        <linearGradient id="patternTone" x1="0" y1="0" x2="1" y2="1">
          <stop offset="0" stop-color="#8fa3d8"/>
          <stop offset="0.5" stop-color="#3f8fcf"/>
          <stop offset="1" stop-color="#7f97d2"/>
        </linearGradient>
      </defs>
      <polygon points="0,0 81,0 196,255 361,350 361,540 521,798 0,798" fill="url(#patternTone)" opacity="0.55"/>
    </svg>

    <section class="details">
      <p class="line caps small" style="top:70px">We invite you to join us in celebration</p>
      <p class="line caps small" style="top:112px">as our dear son</p>
      <h1 class="line honoree" style="top:128px">Ethan Samuel Adler</h1>
      <p class="line caps small" style="top:196px">is called to the Torah as a Bar Mitzvah</p>
      <p class="line caps medium" style="top:234px">Saturday, June 13, 2015</p>
      <p class="line caps small" style="top:262px">at ten o’clock in the morning</p>
      <p class="line caps medium" style="top:296px">Temple Beth Ariel</p>
      <p class="line caps medium" style="top:323px">1280 Linden Road,</p>
      <p class="line caps medium" style="top:350px">Maple Grove, Ohio 44099</p>
      <p class="line caps small" style="top:380px">luncheon to follow</p>
      <p class="line caps small" style="top:416px">party at seven o’clock in the evening</p>
      <p class="line caps medium" style="top:443px">The Linden Room, 22 Park Avenue</p>
      <p class="line hosts" style="top:488px">Laura <span class="amp">&amp;</span> Mark Adler</p>
      <svg class="emblem" viewBox="0 0 66 70" role="img" aria-label="Small blue six-pointed star emblem">
        <rect x="13" y="15" width="40" height="40" fill="#1a6ea8" opacity="0.6"/>
      </svg>
      <p class="line rsvp-deadline" style="top:650px">RSVP by May 31, 2015</p>
      <p class="line contact" style="top:685px">Laura at lauraadler@example.com</p>
      <p class="line contact phone" style="top:720px">or
        <svg class="phone-icon" width="28" height="28" viewBox="0 0 28 28" aria-hidden="true">
          <circle cx="14" cy="14" r="12.5" fill="none" stroke="#c6c9d4" stroke-width="1.8"/>
          <path d="M10 7 q-3 7 3 14 l2-1.5 -2-3 -1.5 1 q-2-3-0.5-6.5 l1.8 0.2 0.5-3.5z" fill="#c6c9d4"/>
        </svg>555.014.2298</p>
    </section>
  </main>
</body>
</html>
```